Risk Management Company in need of Business Card Design

We sell risk management insurance to Lenders (Banks, Credit Unions, Real Estate Trust).

We need a very clean, professional card that will leave a great impression.

We are looking to use a blue color for our logo on the card (Preferably close to royal blue but are open to looking at navy blue or any darker blues as well).

Please see the logo attached to get an idea. We are open to writing Harbor Vault Under the logo or next to the logo. Really whatever looks best.

Target Market(s)

Banks, Credit Unions, Real Estate Trusts

Industry/Entity Type

Insurance

Contact Information for Business Card

Name: Mark Dunstan
Title: Regional Sales Director
Email: mdunstan@harborvault-example.net
C:555-318-2047
D:555-674-1192
800-555-0147 Ext.312
F:555-829-6630 (We would like to see some cards without the fax number as well to compare)

Company Name: Harbor Vault
Website: www.harborvault-example.net

Address: 418 E. Marlowe St. Suite 140, Wrenfield, KV 21286 (Preferably written on the bottom of the card in small print.)

Colors
0355a3
0455a3

Requirements
Nice to have
• We would like to see a couple of where the back has the logo in reverse colors (Logo White, Background Blue)

```html
<!DOCTYPE html>
<html lang="en">
<head>
<meta charset="utf-8">
<title>Harbor Vault — Business Cards</title>
<link rel="stylesheet" href="https://fonts.googleapis.com/css2?family=Cinzel:wght@400;600;700&display=swap">
<style>
  :root {
    --navy: #23234f;
    --paper: #ffffff;
    --backdrop: #e9e9ec;
    --ink: #23234f;
    --rule-light: #ffffff;
  }
  * { box-sizing: border-box; margin: 0; padding: 0; }
  html, body {
    width: 1200px; height: 1000px; overflow: hidden;
    background: var(--backdrop);
    font-family: "Cinzel", serif;
    color: var(--ink);
  }
  .sheet { position: relative; width: 1200px; height: 1000px; }

  .card {
    position: absolute;
    width: 560px; height: 320px;
    background: var(--paper);
    box-shadow: 0 6px 18px rgba(0,0,0,0.18);
    overflow: hidden;
  }
  .card--front-plain { left: 26px;  top: 120px; }
  .card--front-fax   { left: 614px; top: 120px; }
  .card--back        { left: 320px; top: 540px; background: var(--navy); }

  .identity {
    position: absolute; left: 0; top: 0; width: 246px; height: 224px;
    text-align: center;
  }
  .brand {
    position: absolute; left: 0; right: 0; top: 38px;
    display: flex; align-items: center; justify-content: center; gap: 10px;
    font-weight: 600; font-size: 17px; letter-spacing: 2px; color: var(--navy);
  }
  .brand__mark { width: 14px; height: 14px; background: var(--navy); }
  .person__name {
    position: absolute; left: 0; right: 0; top: 140px;
    font-weight: 600; font-size: 22px; letter-spacing: 2px;
  }
  .person__title {
    position: absolute; left: 0; right: 0; top: 174px;
    font-weight: 600; font-size: 11.5px; letter-spacing: 1px;
  }
  .divider-top {
    position: absolute; left: 246px; top: 22px; width: 2px; height: 180px;
    background: var(--navy);
  }

  .contact {
    position: absolute; left: 268px; top: 56px;
    font-size: 13px; letter-spacing: 1.4px; line-height: 17px;
  }
  .contact__email { font-size: 9px; letter-spacing: 0.6px; font-weight: 600; margin-bottom: 2px; }
  .contact__row { display: flex; }
  .contact__label { width: 46px; font-size: 10.5px; font-weight: 600; }

  .band {
    position: absolute; left: 0; bottom: 0; width: 100%; height: 96px;
    background: var(--navy); color: var(--paper);
  }
  .band__web {
    position: absolute; left: 0; top: 0; width: 326px; height: 96px;
    display: flex; align-items: center; justify-content: center;
    font-size: 10.5px; letter-spacing: 2px;
  }
  .band__rule {
    position: absolute; left: 326px; top: 12px; width: 2px; height: 72px;
    background: var(--rule-light);
  }
  .band__address {
    position: absolute; left: 346px; top: 24px;
    font-size: 10.5px; letter-spacing: 1px; line-height: 20px;
  }

  .back__brand {
    position: absolute; inset: 0;
    display: flex; align-items: center; justify-content: center; gap: 22px;
    color: var(--paper); font-size: 40px; font-weight: 600; letter-spacing: 5px;
  }
  .back__mark { width: 30px; height: 30px; background: var(--paper); }
</style>
</head>
<body>
<main class="sheet">

  <section class="card card--front-plain">
    <div class="identity">
      <div class="brand"><span class="brand__mark"></span>Harbor Vault</div>
      <div class="person__name">Mark Dunstan</div>
      <div class="person__title">Regional Sales Director</div>
    </div>
    <div class="divider-top"></div>
    <div class="contact">
      <div class="contact__email">Email: mdunstan@harborvault-example.net</div>
      <div class="contact__row"><span class="contact__label">Cell:</span>555-318-2047</div>
      <div class="contact__row"><span class="contact__label">D:</span>555-674-1192</div>
      <div class="contact__row"><span class="contact__label"></span>800-555-0147</div>
    </div>
    <div class="band">
      <div class="band__web">www.harborvault-example.net</div>
      <div class="band__rule"></div>
      <div class="band__address">418 E. Marlowe St.<br>Suite 140, Wrenfield, KV 21286</div>
    </div>
  </section>

  <section class="card card--front-fax">
    <div class="identity">
      <div class="brand"><span class="brand__mark"></span>Harbor Vault</div>
      <div class="person__name">Mark Dunstan</div>
      <div class="person__title">Regional Sales Director</div>
    </div>
    <div class="divider-top"></div>
    <div class="contact">
      <div class="contact__email">Email: mdunstan@harborvault-example.net</div>
      <div class="contact__row"><span class="contact__label">Cell:</span>555-318-2047</div>
      <div class="contact__row"><span class="contact__label">D:</span>555-674-1192</div>
      <div class="contact__row"><span class="contact__label"></span>800-555-0147</div>
      <div class="contact__row"><span class="contact__label">F:</span>555-829-6630</div>
    </div>
    <div class="band">
      <div class="band__web">www.harborvault-example.net</div>
      <div class="band__rule"></div>
      <div class="band__address">418 E. Marlowe St.<br>Suite 140, Wrenfield, KV 21286</div>
    </div>
  </section>

  <section class="card card--back">
    <div class="back__brand"><span class="back__mark"></span>Harbor Vault</div>
  </section>

</main>
</body>
</html>
```